Design website for new email startup

We are starting a company called Posta.QZ (it will live at http://posta.qz.example).

We would like the main landing page for our site designed. We have provided a very simple wireframe to help provide direction for the content it should include, but we do not expect the designers to adhere to it at all - we encourage unique ideas. There is some sample text in the wireframe - this does not have to be used, but may provide ideas.

We provide an easy way for people to manage email for a custom domain name. For example if you own "myfamilyword.example" you can point your DNS records to us and we'll make it easy to have emails addressed to your domain get forwarded to your existing email (vexmail, etc). Folks running blogs, and other small sites can quickly setup email addresses for their domains and manage them in one place.

(For technical folks, we have you point your dns mx records to us, hence the name. That way all your email hits us and we can redirect it wherever you want. We make it easy to manage a single domain or a bunch of domains. Many domain registrars offer this service for a fee, and have clumsy management tools. We provide a robust simple toolset for free, as well as premium options).

The goal of the landing page is to get folks into the signup flow. The second priority flow is to have them take a look at the premium plan offerings.

We may offer the winning designer additional work for the remainder of the site design.
Updates

I've changed this project to a committed payment.  It is no longer refundable.  Thank you.

Target Market(s)

Bloggers, podcasters, designers, app developers - people who are a little tech savvy.

Industry/Entity Type

It Company

Font styles to use
Sans Serif

Colors

Designer to choose colors to be used in the design.

Requirements
Must have
• A full fidelity mockup (comp) of the landing page including the source file (psd, ai, etc).

Some sort of logo treatment for the posta.qz brand

A call to action for signup, such as the suggested 'Get Started Here'
Nice to have
• A hip startup feel

Incorporation of the email theme

Give the impression it is simple, easy and fast

```html
<!DOCTYPE html>
<html lang="en">
<head>
<meta charset="utf-8">
<title>Posta.QZ — We Make Email Easy</title>
<link href="https://fonts.googleapis.com/css2?family=Arimo:wght@700&family=Open+Sans:wght@400&family=Roboto+Condensed:wght@400;500&display=swap" rel="stylesheet">
<style>
:root{
  --brand-blue:#2385c7;
  --accent-orange:#f45d00;
  --ink:#1e1e1e;
  --page-white:#ffffff;
  --band-grey:#f1f1f1;
  --rule-grey:#dcdcdc;
  --footer-dark:#2d2d2d;
  --footer-text:#f2f2f2;
  --icon-grey:#8a8a8a;
}
*{margin:0;padding:0;box-sizing:border-box}
html,body{width:1200px;height:763px;overflow:hidden;background:var(--page-white)}
.page{position:relative;width:1200px;height:763px;overflow:hidden;font-family:"Open Sans",Arial,sans-serif;color:var(--ink)}

.site-header{position:absolute;left:0;top:0;width:1200px;height:73px;background:var(--brand-blue);box-shadow:0 2px 2px rgba(0,0,0,.12)}
.brand{position:absolute;left:159px;top:14px;font-family:"Arimo",Arial,sans-serif;font-weight:700;font-size:35px;line-height:40px;color:var(--page-white);letter-spacing:-.3px}
.main-nav{position:absolute;left:690px;top:17px;display:flex;gap:6px}
.nav-item{width:113px;height:39px;border:2px solid var(--page-white);border-bottom-width:4px;color:var(--page-white);font-family:"Roboto Condensed",Arial,sans-serif;font-weight:500;font-size:14.5px;display:flex;align-items:center;justify-content:center;gap:6px;text-decoration:none}
.nav-item.is-active{background:var(--page-white);color:var(--brand-blue);border-bottom-width:2px}

.hero{position:absolute;left:0;top:73px;width:1200px;height:321px;background:var(--page-white);border-bottom:1px solid var(--rule-grey)}
.hero-title{position:absolute;left:160px;top:43px;font-family:"Arimo",Arial,sans-serif;font-weight:700;font-size:43.5px;line-height:50px;color:var(--brand-blue);letter-spacing:.2px}
.hero-points{position:absolute;left:159px;top:107px;width:490px;list-style:none}
.hero-points li{position:relative;padding-left:30px;font-size:16px;line-height:20.5px;margin-bottom:10px}
.hero-points li svg{position:absolute;left:0;top:0}
.hero-actions{position:absolute;left:159px;top:243px;display:flex;gap:3px}
.btn{height:37px;display:flex;align-items:center;justify-content:center;font-family:"Roboto Condensed",Arial,sans-serif;font-size:17.5px;color:var(--page-white);text-decoration:none}
.btn-plans{width:146px;background:var(--brand-blue)}
.btn-start{width:146px;background:var(--accent-orange)}
.hero-photo{position:absolute;left:716px;top:0;width:321px;height:321px;background:linear-gradient(180deg,#f4f4f4 0%,#d9d6d4 35%,#4d4a49 70%,#3c3a3a 100%)}

.features{position:absolute;left:0;top:394px;width:1200px;height:305px;background:var(--band-grey)}
.feature{position:absolute;top:52px;width:279px}
.feature:nth-child(1){left:159px}
.feature:nth-child(2){left:461px}
.feature:nth-child(3){left:762px}
.feature-photo{width:279px;height:138px}
.photo-team{background:linear-gradient(135deg,#8c8f92 0%,#c9ccd0 45%,#e6e8ea 100%)}
.photo-web{background:radial-gradient(ellipse at 60% 55%,#d6dff0 0%,#6a7eb5 45%,#1e2a66 100%)}
.photo-support{background:linear-gradient(90deg,#c6c9cf 0%,#e4e6ea 55%,#f2f2f3 100%)}
.feature-text{margin-top:15px;font-size:14.5px;line-height:17.5px;color:var(--ink)}
.feature-link{display:block;margin-top:10px;margin-left:-2px;font-size:14.5px;line-height:17px;color:var(--accent-orange);text-decoration:none}

.site-footer{position:absolute;left:0;top:699px;width:1200px;height:64px;background:var(--footer-dark);color:var(--footer-text);font-size:13px}
.footer-nav{position:absolute;left:159px;top:22px;display:flex;gap:8px}
.footer-nav a{color:var(--footer-text);text-decoration:none}
.footer-nav span{color:var(--footer-text)}
.footer-legal{position:absolute;left:691px;top:21px;display:flex;gap:10px}
.footer-social{position:absolute;left:993px;top:24px;display:flex;gap:8px}
.social-dot{width:15px;height:15px;border-radius:50%;background:var(--icon-grey)}
</style>
</head>
<body>
<div class="page">
  <header class="site-header">
    <div class="brand">Posta.QZ</div>
    <nav class="main-nav">
      <a class="nav-item is-active" href="#">HOW IT WORK</a>
      <a class="nav-item" href="#">SUPPORT</a>
      <a class="nav-item" href="#">LOGIN
        <svg width="11" height="11" viewBox="0 0 11 11" aria-hidden="true"><circle cx="5.5" cy="5.5" r="4.7" fill="none" stroke="currentColor" stroke-width="1"/><path d="M3.3 4.4h4.4L5.5 6.9z" fill="currentColor"/></svg>
      </a>
    </nav>
  </header>

  <section class="hero">
    <h1 class="hero-title">WE MAKE EMAIL EASY</h1>
    <ul class="hero-points">
      <li><svg width="20" height="20" viewBox="0 0 20 20" aria-hidden="true"><rect width="20" height="20" rx="4" fill="#111"/><path d="M5 6h5l-2-2.5M5 6v8h5l-2 2.5M10 6l5 4-5 4" fill="none" stroke="#fff" stroke-width="1.3" stroke-linejoin="round"/></svg>Give us five minutes and we'll get you email from your domain</li>
      <li><svg width="20" height="20" viewBox="0 0 20 20" aria-hidden="true"><rect width="20" height="20" rx="4" fill="#111"/><path d="M5 6h5l-2-2.5M5 6v8h5l-2 2.5M10 6l5 4-5 4" fill="none" stroke="#fff" stroke-width="1.3" stroke-linejoin="round"/></svg>Easily forward mail from your custom domain name wherever you want it</li>
      <li><svg width="20" height="20" viewBox="0 0 20 20" aria-hidden="true"><rect width="20" height="20" rx="4" fill="#111"/><path d="M5 6h5l-2-2.5M5 6v8h5l-2 2.5M10 6l5 4-5 4" fill="none" stroke="#fff" stroke-width="1.3" stroke-linejoin="round"/></svg>You take the mail, we'll keep the spam</li>
    </ul>
    <div class="hero-actions">
      <a class="btn btn-plans" href="#">Compare Plans</a>
      <a class="btn btn-start" href="#">Get Started Free</a>
    </div>
    <div class="hero-photo" role="img" aria-label="Photo of a smiling businesswoman holding a large white at-sign"></div>
  </section>

  <section class="features">
    <article class="feature">
      <div class="feature-photo photo-team" role="img" aria-label="Photo of two colleagues looking at a laptop"></div>
      <p class="feature-text">How to configure your SkyShield DNS to use posta.qz</p>
      <a class="feature-link" href="#">Learn More &nbsp;&gt;&gt;</a>
    </article>
    <article class="feature">
      <div class="feature-photo photo-web" role="img" aria-label="Photo of a tiny businessman standing on a web address"></div>
      <p class="feature-text">Use posta.qz with your NameNest domain registratoion for reliable email forwarding</p>
      <a class="feature-link" href="#">Learn More &nbsp;&gt;&gt;</a>
    </article>
    <article class="feature">
      <div class="feature-photo photo-support" role="img" aria-label="Photo of a support agent wearing a headset"></div>
      <p class="feature-text">24*7 Support&nbsp; : 1800 555 010<br>Our Email ID &nbsp;&nbsp;: support@posta.qz</p>
      <a class="feature-link" href="#">Click Here Get in Touch &gt;&gt;</a>
    </article>
  </section>

  <footer class="site-footer">
    <nav class="footer-nav">
      <a href="#">Home</a><span>-</span>
      <a href="#">About</a><span>-</span>
      <a href="#">Contact</a><span>-</span>
      <a href="#">How it Work</a><span>-</span>
      <a href="#">Contact us</a>
    </nav>
    <div class="footer-legal">
      <span>© Copytight 2014</span><span>-</span><span>Privacy Policy</span><span>-</span><span>Disclaimer</span>
    </div>
    <div class="footer-social">
      <span class="social-dot" role="img" aria-label="Social network link"></span>
      <span class="social-dot" role="img" aria-label="Social network link"></span>
    </div>
  </footer>
</div>
</body>
</html>
```